Website for software company "velbra"

We need a website for our software company/startup named "velbra". We are developing several products (currently 3 standard-software products) which are all in different sectors, but all our products are available for Laptops/PC/Mobile Phones/Tablets, ... We do also create custom software and support our customers with consulting to optimize their processes.
We already have a Logo which you can find in the attached files.
We are a young team of 4 members (two founders and 2 employees).

To get an idea of our products -> the first one is a planning software for healthcare organizations (eg. Mercyway, firebrigade, pharmacy), the second one is a booking software for sport clubs and the third one is a competition software for sports hunting. You see very diverse. Include or ignore this info of our products as you like.

The design has to be a bootstrap 4 (or higher) design. We have licenced FontAwesome as iconset. Responsive design should come without saying.

Coding

Coded - Design and coding required

Number of Pages Required

5+ page

Font styles to use
Sans Serif

Requirements
Must have
• Starting page, product pages, news section, contact, team, services

```html
<!DOCTYPE html>
<html lang="en">
<head>
<meta charset="utf-8">
<title>Velbra — Software</title>
<link href="https://fonts.googleapis.com/css2?family=Montserrat:wght@400;500;600&display=swap" rel="stylesheet">
<style>
:root{
  --orange:#f47c2c;
  --orange-soft:#f6a46e;
  --dark:#2a2f37;
  --text:#3a3f47;
  --muted:#7d8289;
  --light:#f5f6f8;
  --ice:#e6f0f7;
  --white:#ffffff;
}
*{margin:0;padding:0;box-sizing:border-box}
html,body{width:1200px;height:4286px;overflow:hidden}
body{position:relative;font-family:'Montserrat',sans-serif;color:var(--text);background:var(--white)}
.abs{position:absolute}
.brand{font-weight:600;color:var(--dark);letter-spacing:2px;display:flex;align-items:center;gap:14px}
.brand .mark{width:.8em;height:.8em;background:var(--orange)}
.btn{position:absolute;border:1.5px solid var(--dark);color:var(--dark);font-size:16px;font-weight:500;text-transform:uppercase;display:flex;align-items:center;justify-content:center;letter-spacing:.3px;background:transparent}
.section-title{position:absolute;left:0;width:1200px;text-align:center;font-size:38px;font-weight:500;color:var(--dark);letter-spacing:1px}

/* hero */
.hero{position:absolute;left:0;top:0;width:1200px;height:704px;background:var(--light);overflow:hidden}
.nav{position:absolute;top:62px;right:110px;display:flex;gap:24px;font-size:16px;font-weight:500;color:var(--dark)}
.nav .active{color:var(--orange)}
.hero-title{position:absolute;left:107px;top:228px;font-size:66px;font-weight:500;color:var(--dark);letter-spacing:1px}
.hero-lead{position:absolute;left:111px;top:338px;width:400px;font-size:19px;line-height:35px;color:var(--text)}
.hero-photo{position:absolute;left:561px;top:100px;width:527px;height:551px;background:linear-gradient(160deg,#f1e6dc 0%,#f3b485 55%,#e9e9ea 100%)}

/* welcome */
.welcome-title{position:absolute;left:111px;top:790px;font-size:38px;font-weight:500;line-height:54px;color:var(--dark);letter-spacing:1px}
.play{position:absolute;left:110px;top:936px;width:72px;height:72px;border-radius:50%;background:#fbd8c2;display:flex;align-items:center;justify-content:center}
.play span{width:54px;height:54px;border-radius:50%;background:var(--orange);display:flex;align-items:center;justify-content:center}
.welcome-text{position:absolute;left:479px;top:788px;width:612px;font-size:15.5px;line-height:27.5px;color:var(--muted)}

/* services */
.services{position:absolute;left:0;top:1112px;width:1200px;height:549px;background:var(--light)}
.card{position:absolute;top:1295px;width:232px;height:291px;border-radius:6px;background:linear-gradient(180deg,#f6f8fa 0%,#e2eef6 100%);text-align:center}
.card .corner{position:absolute;left:0;top:0;width:0;height:0;border-top:36px solid var(--dark);border-right:36px solid transparent}
.card .corner.hot{border-top-color:var(--orange)}
.card svg{position:absolute;left:96px;top:44px}
.card h3{position:absolute;left:0;top:110px;width:100%;font-size:22px;font-weight:500;line-height:30px;color:var(--dark)}
.card p{position:absolute;left:14px;top:184px;width:204px;font-size:16px;line-height:23.5px;color:var(--muted)}

/* products */
.product h3{position:absolute;font-size:29px;font-weight:500;line-height:43px;color:var(--dark)}
.product p{position:absolute;width:430px;font-size:16.4px;line-height:26.6px;color:var(--text)}
.photo-circle{position:absolute;border-radius:50%}
.screen{position:absolute;border:2px solid #d9dde2;border-radius:10px;background:#f4f6f8}

/* why */
.why{position:absolute;left:0;top:3303px;width:1200px;height:544px;background:var(--orange);overflow:hidden}
.why-photo{position:absolute;left:0;top:0;width:616px;height:544px;background:linear-gradient(135deg,#8b7a6a 0%,#3f444b 55%,#c9b7a6 100%);clip-path:polygon(0 0,433px 0,616px 544px,0 544px)}
.why h2{position:absolute;left:636px;top:70px;font-size:38px;font-weight:500;color:var(--white);letter-spacing:1px}
.perk{position:absolute;display:flex;align-items:center;gap:16px;color:var(--white);font-size:20px;font-weight:500;line-height:28px}
.perk .ring{width:80px;height:80px;border-radius:50%;border:2px solid var(--white);display:flex;align-items:center;justify-content:center;flex:none}

/* footer */
.footer h4{position:absolute;top:3913px;font-size:17px;font-weight:600;color:var(--dark)}
.footer ul{position:absolute;top:3957px;list-style:none;font-size:16px;line-height:29px;color:var(--muted)}
.contact-line{position:absolute;left:870px;display:flex;gap:12px;font-size:16px;line-height:29px;color:var(--muted)}
.rule{position:absolute;left:111px;top:4188px;width:977px;height:1px;background:#dcdfe3}
.copy{position:absolute;left:111px;top:4225px;font-size:15px;color:var(--muted)}
.social{position:absolute;top:4216px;width:40px;height:40px;border-radius:50%;border:1.5px solid var(--orange)}
</style>
</head>
<body>

<!-- Hero -->
<header class="hero">
  <svg class="abs" style="left:0;top:0" width="1200" height="704" aria-hidden="true">
    <polygon points="308,704 990,0 1200,0 1200,704" fill="#e3eef6"/>
  </svg>
  <div class="brand abs" style="left:111px;top:40px;font-size:56px"><span class="mark"></span>VELBRA</div>
  <nav class="nav">
    <span class="active">HOME</span><span>ABOUT</span><span>SERVICES</span><span>PRODUCTS</span><span>TEAM</span><span>NEWS</span><span>CONTACT</span>
  </nav>
  <h1 class="hero-title">VELBRA</h1>
  <p class="hero-lead">We are developing several products which are all in different sectors.</p>
  <a class="btn" style="left:111px;top:438px;width:288px;height:58px">Request a consultation</a>
  <div class="hero-photo" role="img" aria-label="Smiling doctor in a white coat holding a tablet"></div>
</header>

<!-- Welcome -->
<section>
  <h2 class="welcome-title">WELCOME TO<br>VELBRA</h2>
  <div class="play"><span>
    <svg width="20" height="22" viewBox="0 0 20 22" aria-hidden="true"><path d="M3 2 L18 11 L3 20 Z" fill="#fff"/></svg>
  </span></div>
  <p class="welcome-text">Nam libero tempore, cum soluta nobis est eligendi optio cumque nihil imp edit quo minus id quod maxime placeat facere possimus, omnis voluptasa ssumenda est, omnis dolor repellendus. Temporibus autem quibusdam et aut officiis debitis aut rerum necessitatibus saepe eveniet ut et voluptates repudiandae sint et molestiae recusandae.</p>
  <a class="btn" style="left:481px;top:954px;width:143px;height:53px">Read more</a>
</section>

<!-- Services -->
<section class="services"></section>
<h2 class="section-title" style="top:1183px">SERVICES</h2>

<div class="card" style="left:111px">
  <span class="corner"></span>
  <svg width="40" height="36" viewBox="0 0 40 36" fill="none" stroke="#f47c2c" stroke-width="3"><ellipse cx="16" cy="13" rx="13" ry="10"/><path d="M8 21 L5 29 L14 23"/><path d="M30 9 C37 11 39 18 34 23 L36 30 L28 25"/></svg>
  <h3>Software<br>consulting</h3>
  <p>At vero eos et accus amus et iusto odio dinis si mos duci muq.</p>
</div>
<div class="card" style="left:359px">
  <span class="corner hot"></span>
  <svg width="40" height="40" viewBox="0 0 40 40" fill="none" stroke="#f47c2c" stroke-width="4"><path d="M6 6 L34 34 M34 6 L6 34"/><path d="M4 14 V4 H14 M26 4 H36 V14 M36 26 V36 H26 M14 36 H4 V26" stroke-width="3.5"/></svg>
  <h3>Software<br>outsourcing</h3>
  <p>At vero eos et accus amus et iusto odio dinis si mos duci muq.</p>
</div>
<div class="card" style="left:607px">
  <span class="corner"></span>
  <svg width="44" height="40" viewBox="0 0 44 40" fill="none" stroke="#f47c2c" stroke-width="4"><circle cx="15" cy="22" r="7"/><path d="M15 9 V13 M15 31 V35 M2 22 H6 M24 22 H28 M6 13 L9 16 M21 28 L24 31 M6 31 L9 28 M21 16 L24 13"/><circle cx="34" cy="10" r="4" stroke-width="3"/><circle cx="34" cy="30" r="4" stroke-width="3"/></svg>
  <h3>Custom software<br>development</h3>
  <p>At vero eos et accus amus et iusto odio dinis si mos duci muq.</p>
</div>
<div class="card" style="left:855px">
  <span class="corner"></span>
  <svg width="40" height="38" viewBox="0 0 40 38" fill="none" stroke="#f47c2c" stroke-width="4"><path d="M5 26 V20 A15 15 0 0 1 35 20 V26"/><rect x="4" y="22" width="7" height="12" rx="2" fill="#f47c2c"/><rect x="29" y="22" width="7" height="12" rx="2" fill="#f47c2c"/></svg>
  <h3>Support and<br>evolution</h3>
  <p>At vero eos et accus amus et iusto odio dinis si mos duci muq.</p>
</div>

<!-- Products -->
<h2 class="section-title" style="top:1732px">PRODUCTS</h2>

<article class="product">
  <h3 style="left:111px;top:1893px">Planning software for<br>healthcare organizations</h3>
  <p style="left:111px;top:2007px">Nam libero tempore, cum soluta nobis est eligendi optio cumque nihil impedit quo minus id quomaxi me placeat facere possimus, omnis voluptas assuen da est, omnis dolor repellendus emporibus autem quibusdam et aut officiis debitis.</p>
  <a class="btn" style="left:111px;top:2175px;width:144px;height:52px">Read more</a>
  <div class="photo-circle" role="img" aria-label="Pharmacist holding a tablet in front of medicine shelves" style="left:712px;top:1873px;width:376px;height:376px;background:linear-gradient(135deg,#e7ecef 0%,#b9c9cf 50%,#6f8e8b 100%)"></div>
  <div class="screen" role="img" aria-label="Health planning app shown on a phone" style="left:577px;top:1843px;width:208px;height:434px;border-radius:22px;background:#ffffff"></div>
</article>

<article class="product">
  <div class="photo-circle" role="img" aria-label="Golfers on a practice green" style="left:106px;top:2340px;width:380px;height:380px;background:linear-gradient(135deg,#c9c2b7 0%,#8d9a84 50%,#4e5a4a 100%)"></div>
  <div class="screen" role="img" aria-label="Booking calendar software shown on a tablet" style="left:327px;top:2546px;width:289px;height:203px;background:#ffffff"></div>
  <h3 style="left:676px;top:2372px">Booking software for<br>sport clubs</h3>
  <p style="left:676px;top:2486px">Nam libero tempore, cum soluta nobis est eligendi optio cumque nihil impedit quo minus id quomaxi me placeat facere possimus, omnis voluptas assuen da est, omnis dolor repellendus emporibus autem quibusdam et aut officiis debitis.</p>
  <a class="btn" style="left:676px;top:2656px;width:143px;height:52px">Read more</a>
</article>

<article class="product">
  <h3 style="left:111px;top:2853px">Competition software for<br>sports hunting</h3>
  <p style="left:111px;top:2967px">Nam libero tempore, cum soluta nobis est eligendi optio cumque nihil impedit quo minus id quomaxi me placeat facere possimus, omnis voluptas assuen da est, omnis dolor repellendus emporibus autem quibusdam et aut officiis debitis.</p>
  <a class="btn" style="left:111px;top:3135px;width:144px;height:53px">Read more</a>
  <div class="photo-circle" role="img" aria-label="Sport shooter aiming under a cloudy sky in a field" style="left:714px;top:2834px;width:374px;height:374px;background:linear-gradient(180deg,#a9b4c0 0%,#7e8c99 50%,#5d6e45 100%)"></div>
  <div class="screen" role="img" aria-label="Competition results software shown on a laptop" style="left:555px;top:2962px;width:306px;height:214px;background:#ffffff;border-radius:6px"></div>
  <div class="abs" style="left:513px;top:3176px;width:390px;height:8px;border-radius:0 0 8px 8px;background:#c9cdd2"></div>
</article>

<!-- Why choose -->
<section class="why">
  <div class="why-photo" role="img" aria-label="Developer with glasses working at a computer showing code"></div>
  <h2>WHY CHOOSE VELBRA</h2>
  <div class="perk" style="left:636px;top:166px"><span class="ring"><svg width="34" height="34" viewBox="0 0 34 34" fill="none" stroke="#fff" stroke-width="3"><circle cx="17" cy="17" r="14"/><path d="M17 9 V17 H12"/></svg></span>On time,<br>on budget</div>
  <div class="perk" style="left:897px;top:166px"><span class="ring"><svg width="34" height="34" viewBox="0 0 34 34" fill="#fff"><rect x="3" y="14" width="7" height="16" rx="1"/><path d="M12 14 L18 4 C21 4 22 6 21 9 L20 13 H29 C31 13 32 15 31 17 L28 28 C27 30 26 30 24 30 H12 Z"/></svg></span>Smart<br>Features</div>
  <div class="perk" style="left:636px;top:278px"><span class="ring"><svg width="38" height="34" viewBox="0 0 44 40" fill="none" stroke="#fff" stroke-width="4"><circle cx="15" cy="22" r="7"/><path d="M15 9 V13 M15 31 V35 M2 22 H6 M24 22 H28 M6 13 L9 16 M21 28 L24 31 M6 31 L9 28 M21 16 L24 13"/><circle cx="34" cy="10" r="4" stroke-width="3"/><circle cx="34" cy="30" r="4" stroke-width="3"/></svg></span>Customization</div>
  <div class="perk" style="left:897px;top:262px"><span class="ring"><svg width="38" height="32" viewBox="0 0 38 32" fill="#fff"><circle cx="19" cy="9" r="6"/><circle cx="7" cy="12" r="4"/><circle cx="31" cy="12" r="4"/><path d="M9 30 C9 20 29 20 29 30 Z"/><path d="M1 28 C1 20 9 19 11 21 L8 28 Z M37 28 C37 20 29 19 27 21 L30 28 Z"/></svg></span>User<br>Friendly</div>
  <div class="perk" style="left:636px;top:372px"><span class="ring"><svg width="34" height="32" viewBox="0 0 40 38" fill="none" stroke="#fff" stroke-width="4"><path d="M5 26 V20 A15 15 0 0 1 35 20 V26"/><rect x="4" y="22" width="7" height="12" rx="2" fill="#fff"/><rect x="29" y="22" width="7" height="12" rx="2" fill="#fff"/></svg></span>Guiding you<br>beyond the<br>basics</div>
  <div class="perk" style="left:897px;top:370px"><span class="ring"><svg width="28" height="34" viewBox="0 0 28 34" fill="none" stroke="#fff" stroke-width="3"><path d="M14 2 L26 6 V16 C26 24 20 30 14 32 C8 30 2 24 2 16 V6 Z"/><path d="M14 2 V32 C20 30 26 24 26 16 V6 Z" fill="#fff"/></svg></span>Secure &amp;<br>Privacy</div>
</section>

<!-- Footer -->
<footer class="footer">
  <div class="brand abs" style="left:111px;top:3930px;font-size:66px"><span class="mark"></span>VELBRA</div>
  <h4 style="left:511px">Quick Links</h4>
  <ul style="left:511px"><li>Home</li><li>About</li><li>Services</li><li>Products</li><li>Team</li><li>News</li><li>Contact</li></ul>
  <h4 style="left:699px">Platforms</h4>
  <ul style="left:699px"><li>Mobile</li><li>Tablet</li><li>Desktop</li></ul>
  <h4 style="left:870px">Contact Us</h4>
  <div class="contact-line" style="top:3957px">
    <svg width="10" height="28" viewBox="0 0 10 28"><path d="M5 6 C2 6 0 8 0 11 C0 14 5 20 5 20 C5 20 10 14 10 11 C10 8 8 6 5 6 Z" fill="#f47c2c"/><circle cx="5" cy="11" r="2" fill="#fff"/></svg>
    <span>1420 N. Birch Ave Suite 210,<br>Fairview area, TX 75000</span>
  </div>
  <div class="contact-line" style="top:4042px">
    <svg width="14" height="28" viewBox="0 0 14 28"><path d="M2 8 L5 7 L7 11 L5 13 C6 15 7 17 9 18 L11 16 L14 18 L13 21 C7 21 2 15 2 8 Z" fill="#f47c2c"/></svg>
    <span>1 555 010 2040</span>
  </div>
  <div class="contact-line" style="top:4100px">
    <svg width="16" height="28" viewBox="0 0 16 28"><rect x="0" y="9" width="16" height="11" rx="1" fill="#f47c2c"/><path d="M1 10 L8 15 L15 10" stroke="#fff" stroke-width="1.5" fill="none"/></svg>
    <span>info@velbra.com</span>
  </div>
  <div class="rule"></div>
  <p class="copy">© 2022, Velbra. All rights reserved.</p>
  <span class="social" style="left:958px"></span>
  <span class="social" style="left:1003px"></span>
  <span class="social" style="left:1047px"></span>
</footer>

</body>
</html>
```